KTV Brochure redesign

We need a brochure redesign for a new company based in UK. Meridale Talent Partners (KTV) is a new generation of headhunters within the Payment & Card industries across the EMEA & Asia Pac including the Emerging Markets. Our current design was designed by myself, I am looking for a more professional touch.

Target Market(s)

ePayment & Card industries

Industry/Entity Type

It Company

Font styles to use
Serif

Requirements
Must have
• Must be engaging, clear and clean. The industries are very fast paced, high tech business such as CoinDash, Tellmaro, ZenithTill
Nice to have
• Colour, cool trendy high tech design, Please keep logo. Feel free to cut text to improve design
Should not have
• Design should be simple child like, it must be better than what i already have...

```html
<!DOCTYPE html>
<html lang="en">
<head>
<meta charset="utf-8">
<title>KTV – New Generation of Headhunters</title>
<link href="https://fonts.googleapis.com/css2?family=Work+Sans:wght@300&family=Tinos&display=swap" rel="stylesheet">
<style>
  :root {
    --brand-red: #d7252f;
    --band-start: #d92a2f;
    --band-mid: #ee7a22;
    --band-end: #f8b71a;
    --ink: #111111;
    --paper: #ffffff;
    --visual-light: #fbfbfb;
    --visual-mid: #e9e9eb;
    --visual-deep: #d4d5d8;
  }
  * { margin: 0; padding: 0; box-sizing: border-box; }
  html, body { width: 1200px; height: 848px; overflow: hidden; background: var(--paper); }
  .page {
    position: relative;
    width: 1200px;
    height: 848px;
    overflow: hidden;
    background: var(--paper);
    color: var(--ink);
  }
  .top-band {
    position: absolute;
    left: 0; top: 0;
    width: 100%; height: 17px;
    background: linear-gradient(90deg, var(--band-start), var(--band-mid) 55%, var(--band-end));
  }
  .feature-visual {
    position: absolute;
    left: 541px; top: 502px;
    width: 631px; height: 320px;
    background:
      radial-gradient(ellipse at 45% 60%, rgba(215,37,47,0.18), rgba(215,37,47,0) 28%),
      linear-gradient(100deg, var(--paper) 0%, var(--visual-light) 18%, var(--visual-mid) 55%, var(--visual-deep) 100%);
  }
  .decor { position: absolute; left: 0; top: 0; pointer-events: none; }
  .headline {
    position: absolute;
    left: 50px; top: 160px;
    font-family: "Work Sans", "Helvetica Neue", sans-serif;
    font-weight: 300;
    font-size: 63px;
    line-height: 82px;
    letter-spacing: -0.5px;
    text-transform: uppercase;
  }
  .headline .brand { color: var(--brand-red); }
  .intro {
    position: absolute;
    left: 50px; top: 353px;
    width: 780px;
    font-family: "Tinos", "Times New Roman", serif;
    font-size: 11.4px;
    line-height: 15px;
  }
  .intro p + p { margin-top: 14px; }
</style>
</head>
<body>
<main class="page">
  <div class="top-band"></div>

  <div class="feature-visual" role="img" aria-label="Close-up photo of a finger pressing a red 'pay' key on a white keyboard"></div>

  <svg class="decor" width="1200" height="848" viewBox="0 0 1200 848" aria-hidden="true">
    <circle cx="926" cy="670" r="378" fill="none" stroke="var(--brand-red)" stroke-width="1.2"/>
    <circle cx="-43" cy="855" r="150" fill="none" stroke="#333" stroke-width="1"/>
  </svg>

  <h1 class="headline"><span class="brand">KTV</span> – New Generation<br>of Headhunters</h1>

  <section class="intro">
    <p>Meridale Talent Partners (KTV) is a new generation of headhunters. We are entirely focused on innovative, creative and effective talent acquisition and we like to think we are getting rather good at it. Our expertise lies within Card &amp; Payments specific businesses across the EMEA &amp; Asia Pac and we have achieved notable successes internationally.</p>
    <p>Our aim is simple - to become the world’s most respected Card &amp; Payments global headhunters without losing our boutique feel. We will consult, we will advise and we will execute YOUR plan.</p>
    <p>Start working together with KTV today; to find better quality hires for your organisation, faster and more cost effectively.</p>
  </section>
</main>
</body>
</html>
```